Innovative Event Ticketing Start Up. Needs a Web Design

We need a web design for a new company based in London called 'Bandwick'. We are a platform which facilitates the building of groups of customers for events. As more people commit to an event, the price incrementally decreases. We would like there to be an emphasis on the sharing element and the decreasing price with higher participation.

Any quieres please email me at rlvo57@mailtrove.net

Target Market(s)

18-30 year olds who are active and savvy across social media sites

Industry/Entity Type

Events

Number of Pages Required

3 page

Font styles to use
Other font styles liked:
• Phi Roman

Requirements
Must have
• Each event offering runs for a limited time so a countdown timer is also to be included as well as a counter of number of participants (please find example attached).
• The interface needs to have the options for 'Live 'Music', 'Nightlife', 'Festivals', 'Comedy' and 'Everything Else'. Also
• A 'featured' section, for our promoted events
• Social sharing icons for Chatterbarn, Quillow, PingMesh, SMS and Email
• Room the inclusion of a video
• Pages for clients to sign up - registering details ect.
• Content is still being completed, so room available to add when ready
Nice to have
• An interface design we like as a guiding templates on is https://kumvoxapp.com/
• Zamo wordpress theme is also of interest.
• Scroll over clicking for main interface and also for the event once clicked upon.
• Event pages similar desgin to kumvox with same features such as Trelvo Charts but also participant counter and affiliate marketing options.
Should not have
• CMS no longer necessary

```html
<!DOCTYPE html>
<html lang="en">
<head>
<meta charset="utf-8">
<title>Bandwick – Events Together</title>
<link href="https://fonts.googleapis.com/css2?family=Open+Sans:wght@400;600;700&family=Raleway:wght@400;500;600&display=swap" rel="stylesheet">
<style>
:root{
  --orange:#f15a22;
  --orange-soft:#f47a3c;
  --red:#e2202c;
  --pink:#fde3df;
  --ink:#333333;
  --muted:#777777;
  --white:#ffffff;
  --page:#ffffff;
  --hero-top:#1d2b52;
  --hero-mid:#3b4e7f;
  --hero-glow:#d98a3a;
}
*{box-sizing:border-box;margin:0;padding:0}
html,body{width:1200px;height:2168px;overflow:hidden}
body{position:relative;background:var(--page);font-family:"Open Sans",Arial,sans-serif;color:var(--ink)}
.abs{position:absolute}

/* hero */
.hero{left:0;top:0;width:1200px;height:416px;background:linear-gradient(180deg,var(--hero-top) 0%,var(--hero-mid) 45%,var(--hero-glow) 85%,#8a4a22 100%)}
.hero-strip{left:0;top:410px;width:1200px;height:10px;background:var(--orange)}
.nav{left:0;top:0;width:1200px;height:80px;display:flex;align-items:center;padding:0 112px}
.brand{display:flex;align-items:center;gap:10px;color:var(--white);font-weight:700;font-size:26px;letter-spacing:1px}
.brand-mark{width:30px;height:30px;background:var(--orange)}
.menu{display:flex;gap:22px;margin-left:54px;list-style:none}
.menu li{color:var(--white);font-size:13px;padding:0 0 0 22px;border-left:1px solid rgba(255,255,255,.5)}
.menu li:first-child{border-left:none;padding-left:0}
.signup{margin-left:auto;background:var(--white);color:var(--ink);font-size:11px;font-weight:700;padding:7px 12px;border-radius:2px}
.social{left:1168px;top:160px;width:32px;display:flex;flex-direction:column;gap:4px}
.social span{display:block;width:32px;height:26px}
.hero-title{left:0;top:180px;width:1200px;text-align:center;color:var(--white);font-family:"Raleway",sans-serif;font-size:32px;font-weight:500;letter-spacing:1px}
.hero-sub{left:0;top:222px;width:1200px;text-align:center;color:rgba(255,255,255,.85);font-size:12px}
.search{left:360px;top:252px;width:480px;height:40px;background:var(--white);border-radius:2px}
.search svg{position:absolute;right:12px;top:11px}

/* section heads */
.sec-title{left:0;width:1200px;text-align:center;color:var(--orange);font-family:"Raleway",sans-serif;font-size:28px;font-variant:small-caps;letter-spacing:1px}
.sec-sub{left:0;width:1200px;text-align:center;color:var(--muted);font-size:12px}

/* facilities */
.tile{overflow:hidden}
.tile .ph{position:absolute;inset:0}
.tile-label{position:absolute;left:0;right:0;height:40px;background:rgba(255,255,255,.72);color:var(--ink);font-size:15px;display:flex;align-items:center;justify-content:center}

/* collection */
.promo{background:var(--orange);color:var(--white);text-align:center}
.promo h3{font-family:"Raleway",sans-serif;font-weight:500;font-size:20px;margin-top:16px}
.promo-card{position:absolute;left:26px;top:62px;width:256px;height:360px;background:var(--white);color:var(--muted)}
.promo-card p{position:absolute;left:22px;right:22px;top:220px;font-size:11px;line-height:17px;text-align:left}
.count{position:absolute;left:48px;top:40px}
.caption{background:var(--pink);padding:22px 18px}
.caption h4{font-size:16px;font-weight:600;color:var(--ink)}
.caption p{font-size:11px;line-height:17px;color:var(--muted);margin-top:10px;width:190px}
.more{position:absolute;right:18px;bottom:16px;background:var(--red);color:var(--white);font-size:9px;padding:3px 8px}
.hover-card h3{font-family:"Raleway",sans-serif;font-weight:500;font-size:20px;margin-top:40px}
.avatar{position:absolute;left:104px;top:100px;width:110px;height:110px;border-radius:50%;background:radial-gradient(circle,#a8725a,#4a2a20);border:4px solid var(--white)}
.hover-card p{position:absolute;left:40px;right:40px;top:240px;font-size:11px;line-height:17px}

/* contact */
.map{left:0;top:1800px;width:660px;height:262px;background:linear-gradient(135deg,#eef0ea,#e2e6dc 60%,#d8dfd2)}
.contact{left:660px;top:1800px;width:540px;height:262px;background:#f6f6f6}
.ci{position:absolute;display:flex;align-items:flex-start;gap:14px;font-size:11px;line-height:17px;color:var(--muted);width:210px}
.ci svg{flex:none}

/* footer */
.footer{left:0;top:2080px;width:1200px;height:88px}
.footer-text{left:0;top:2116px;width:1200px;text-align:center;color:var(--white);font-size:11px}
</style>
</head>
<body>

<header>
  <div class="abs hero" role="img" aria-label="Night view of London landmarks lit up along the river"></div>
  <div class="abs hero-strip"></div>
  <nav class="abs nav">
    <div class="brand"><span class="brand-mark"></span>BANDWICK</div>
    <ul class="menu">
      <li>Home</li><li>Live</li><li>Music</li><li>Nightlife</li><li>Festivals</li><li>Contact</li>
    </ul>
    <div class="signup">SIGN UP / LOGIN</div>
  </nav>
  <div class="abs social" aria-label="Share links">
    <span style="background:#e23b2e"></span>
    <span style="background:#cc2127"></span>
    <span style="background:#3b9bd8"></span>
    <span style="background:#dd4b39"></span>
    <span style="background:#3b5998"></span>
  </div>
  <h1 class="abs hero-title">WELCOME TO OUR WEBSITE</h1>
  <p class="abs hero-sub">We are a platform which facilitates the building of groups of customers for events.</p>
  <div class="abs search">
    <svg width="18" height="18" viewBox="0 0 18 18"><circle cx="7.5" cy="7.5" r="5.5" fill="none" stroke="#555" stroke-width="2"/><line x1="11.5" y1="11.5" x2="16" y2="16" stroke="#555" stroke-width="2"/></svg>
  </div>
</header>

<section>
  <h2 class="abs sec-title" style="top:430px">Our Facilitates</h2>
  <p class="abs sec-sub" style="top:468px">We are a platform which facilitates the building of groups of customers for events.</p>

  <div class="abs tile" style="left:112px;top:500px;width:310px;height:466px">
    <div class="ph" role="img" aria-label="Concert crowd under stage lights" style="background:linear-gradient(160deg,#6a7bd0,#2b2f6a 60%,#121432)"></div>
    <div class="tile-label" style="top:360px">Live Videos</div>
  </div>
  <div class="abs tile" style="left:440px;top:500px;width:312px;height:226px">
    <div class="ph" role="img" aria-label="Crowd at a weekend party" style="background:linear-gradient(160deg,#c9a48a,#7a4a3a 60%,#3a2420)"></div>
    <div class="tile-label" style="top:162px">This Weekend</div>
  </div>
  <div class="abs tile" style="left:440px;top:740px;width:312px;height:226px">
    <div class="ph" role="img" aria-label="Ceremonial parade in London" style="background:linear-gradient(180deg,#b8c2cc,#8a6f6a 55%,#a02a2a)"></div>
    <div class="tile-label" style="top:162px">Special Offers</div>
  </div>
  <div class="abs tile" style="left:770px;top:500px;width:318px;height:466px">
    <div class="ph" role="img" aria-label="Dancing crowd at a club event" style="background:linear-gradient(160deg,#4a7be0,#6a3aa8 55%,#1c1a40)"></div>
    <div class="tile-label" style="top:400px">Featured Events</div>
  </div>
</section>

<section>
  <h2 class="abs sec-title" style="top:974px">Our Collection</h2>
  <p class="abs sec-sub" style="top:1012px">We are a platform which facilitates the building of groups of customers for events.</p>

  <article class="abs promo" style="left:112px;top:1052px;width:310px;height:448px">
    <h3>Band Together</h3>
    <div class="promo-card" style="left:26px">
      <svg class="count" width="160" height="160" viewBox="0 0 160 160">
        <circle cx="80" cy="80" r="62" fill="none" stroke="#eeeeee" stroke-width="12"/>
        <circle cx="80" cy="80" r="62" fill="none" stroke="#e2202c" stroke-width="12" stroke-dasharray="330 60" transform="rotate(-90 80 80)"/>
        <text x="80" y="86" text-anchor="middle" font-family="Open Sans, sans-serif" font-size="28" font-weight="700" fill="#e2202c">680</text>
        <text x="80" y="104" text-anchor="middle" font-family="Open Sans, sans-serif" font-size="9" fill="#888">people going</text>
      </svg>
      <p>More friends join, the lower the price drops for every ticket in the group.</p>
    </div>
  </article>
  <div class="abs" role="img" aria-label="London skyline at dusk over the river" style="left:112px;top:1514px;width:310px;height:266px;background:linear-gradient(180deg,#4a5fa0,#7a5c8e 55%,#d08a5a)"></div>

  <div class="abs" role="img" aria-label="Guests at a London nightlife party" style="left:440px;top:1052px;width:312px;height:240px;background:linear-gradient(160deg,#8a6a5a,#3a2826)"></div>
  <article class="abs caption" style="left:440px;top:1292px;width:312px;height:128px">
    <h4>London Nightlife</h4>
    <p>Gather your crew for late nights across the city and watch the price fall.</p>
    <span class="more">Read more</span>
  </article>
  <div class="abs" role="img" aria-label="Model walking a fashion runway" style="left:440px;top:1426px;width:312px;height:228px;background:linear-gradient(180deg,#d8d4d6,#9a7a8a 60%,#5a4a5a)"></div>
  <article class="abs caption" style="left:440px;top:1654px;width:312px;height:126px">
    <h4>Riverside Style Weekend</h4>
    <p>Runway events and parties, booked together by groups who share the savings.</p>
    <span class="more">Read more</span>
  </article>

  <div class="abs" role="img" aria-label="Music crowd with raised hands under blue lights" style="left:770px;top:1052px;width:312px;height:240px;background:linear-gradient(160deg,#4a78c8,#1c2a60)"></div>
  <article class="abs caption" style="left:770px;top:1292px;width:312px;height:128px">
    <h4>London Music</h4>
    <p>Live gigs and shows, cheaper every time another fan commits to the night.</p>
    <span class="more">Read more</span>
  </article>
  <article class="abs promo hover-card" style="left:770px;top:1426px;width:312px;height:354px">
    <h3>Scroll over clicking</h3>
    <div class="avatar" role="img" aria-label="Round portrait of an event guest"></div>
    <p>Hover any event to preview the details, price drop and people already going.</p>
  </article>
</section>

<section>
  <div class="abs map" role="img" aria-label="Street map of central London with the venue marked"></div>
  <div class="abs contact">
    <div class="ci" style="left:24px;top:70px">
      <svg width="16" height="20" viewBox="0 0 16 20"><path d="M8 0C3.6 0 0 3.4 0 7.6 0 13 8 20 8 20s8-7 8-12.4C16 3.4 12.4 0 8 0z" fill="#f15a22"/><circle cx="8" cy="7.5" r="3" fill="#fff"/></svg>
      <span>12 Harbour Lane, Southwark, London SE1 4QT</span>
    </div>
    <div class="ci" style="left:284px;top:70px">
      <svg width="20" height="14" viewBox="0 0 20 14"><rect width="20" height="14" fill="#f15a22"/><path d="M0 0l10 8 10-8" fill="none" stroke="#fff" stroke-width="1.5"/></svg>
      <span>rlvo57@mailtrove.net</span>
    </div>
    <div class="ci" style="left:24px;top:150px">
      <svg width="14" height="20" viewBox="0 0 14 20"><rect x="1" y="0" width="12" height="20" rx="2" fill="#f15a22"/><rect x="3" y="3" width="8" height="11" fill="#fff"/></svg>
      <span>+44 20 7946 0381</span>
    </div>
    <div class="ci" style="left:284px;top:150px">
      <svg width="20" height="20" viewBox="0 0 20 20"><circle cx="10" cy="10" r="9" fill="none" stroke="#f15a22" stroke-width="2"/><path d="M1 10h18M10 1c-4 4-4 14 0 18M10 1c4 4 4 14 0 18" fill="none" stroke="#f15a22" stroke-width="1.5"/></svg>
      <span>https://kumvoxapp.com/</span>
    </div>
  </div>
</section>

<footer>
  <svg class="abs footer" width="1200" height="88" viewBox="0 0 1200 88" preserveAspectRatio="none">
    <polygon points="0,0 1200,0 1200,88 0,88" fill="#f15a22"/>
    <polygon points="0,0 60,0 20,88 0,88" fill="#d94a16"/>
    <polygon points="1140,0 1200,0 1200,88 1180,88" fill="#d94a16"/>
  </svg>
  <p class="abs footer-text">© 2015. All Rights Reserved. Bandwick &nbsp;|&nbsp; Terms &amp; Conditions</p>
</footer>

</body>
</html>
```